New solo practice law firm is looking for an elegant, professional, and interactive web design

I need a web design and developer for a new small law firm in Sacramento, California called Dorian Kessly Law, A Professional Corporation. I am a trial lawyer who represents average people facing difficult litigation disputes, including criminal defense as a former prosecutor and civil litigation as a civil litigator. Criminal defense includes domestic violence, battery, assault, drug possession, theft, DUI, etc. Civil litigation includes business disputes, property disputes, employment disputes, family law disputes, and immigration issues. I would like to see web designs that incorporate my logo and use the logo's navy blue and gold colors. I have uploaded the files of my logo to this brief. Please only use the navy blue and gold version. Overall, I want the design to look firm, professional, and elegant.

I plan on having the following pages on my website: (1) Home, (2) Dorian Kessly, (3) Practice Areas, (4) Insights, (5) Contact. I've hand drawn a preliminary sketch concept of what I envision the home page's layout to look like (attached with a text version). I would like your design to keep a similar layout for the homepage and incorporate my logo's colors within it but I am open to creative layout alternatives/ideas. I would like the other pages to have a similar look and feel as the home page. Some of the areas currently in my sketch do not have the full text. You can insert other text for now and I will provide the winner the full text.

In terms of the pictures on the website, I enjoy images of courthouses, columns (example attached but I cannot use this one), and, if possible, images from Sacramento, CA in my background (headshot attached). A plus would be live images that move and also sections of the webpage moving in the viewers view as they scroll down on the page. Also, it would be great to have my logo act as the tab for the website. I can provide other versions of the logo if needed.

I look forward to seeing your Wordpress designs!

People needing legal representation.

Law

Coded - Design and coding required

5+ page

Serif

• Incorporate my logo and my logo's colors.
• Live pictures and images appearing as viewers scroll on page.

```html
<!DOCTYPE html>
<html lang="en">
<head>
<meta charset="utf-8">
<title>Dorian Kessly Law – Home</title>
<link href="https://fonts.googleapis.com/css2?family=Noto+Serif:ital,wght@0,400;0,500;1,400;1,500&family=Rubik:wght@300;400;500&display=swap" rel="stylesheet">
<style>
:root{
  --navy:#1c2a48;
  --navy-deep:#15203a;
  --gold:#a88a55;
  --beige:#f1f0ea;
  --ink:#1d2433;
  --muted:#6b6f78;
  --line:#dcdad2;
  --night:#0c0f15;
  --white:#fff;
}
*{box-sizing:border-box;margin:0;padding:0}
html,body{width:1200px;height:3422px;overflow:hidden}
body{position:relative;background:var(--white);font-family:"Rubik",sans-serif;color:var(--ink)}
.abs{position:absolute}
.serif{font-family:"Noto Serif",serif}
.eyebrow{position:absolute;font-size:7px;letter-spacing:2px;color:var(--gold);text-transform:uppercase}
.eyebrow::before{content:"";position:absolute;left:-34px;top:2px;width:4px;height:4px;border-radius:50%;background:var(--gold)}
.h2{position:absolute;font-family:"Noto Serif",serif;font-size:16px;color:var(--ink)}
.small{position:absolute;font-size:8px;line-height:13px;color:var(--muted)}
.more{position:absolute;font-size:6.5px;letter-spacing:1px;color:var(--gold);text-transform:uppercase}

/* top / hero */
.stage{left:0;top:0;width:1200px;height:590px;background:var(--navy-deep)}
.page-col{left:121px;top:40px;width:1001px;height:3382px;background:var(--white);border-left:1px solid var(--line);border-right:1px solid var(--line)}
.header{left:121px;top:40px;width:1001px;height:49px;background:var(--white)}
.brand{left:205px;top:52px;display:flex;align-items:center;gap:8px;font-family:"Noto Serif",serif;font-size:11px;color:var(--gold)}
.brand i{width:22px;height:22px;border:1.5px solid var(--gold);display:block}
.nav{left:502px;top:61px;display:flex;gap:16px;font-size:8px;color:var(--ink)}
.nav .on{color:var(--gold);position:relative}
.nav .on::after{content:"";position:absolute;left:50%;top:12px;width:3px;height:3px;margin-left:-1.5px;border-radius:50%;background:var(--gold)}
.phone{left:970px;top:59px;font-size:8px;display:flex;gap:6px;align-items:center}
.hero-img{left:121px;top:89px;width:921px;height:501px;background:linear-gradient(160deg,#4a5a80 0%,#2a3a62 40%,#1a2648 75%,#121b36 100%)}
.hero-label{left:240px;top:257px;font-size:7px;color:#d7dbe6;letter-spacing:.5px}
.hero-title{left:240px;top:270px;font-family:"Noto Serif",serif;font-size:23px;line-height:29px;color:var(--white)}
.hero-title em{display:block;color:var(--gold);font-style:italic}
.hero-btn{left:240px;top:393px;width:131px;height:26px;border:1px solid rgba(255,255,255,.7);border-radius:14px;color:var(--white);font-size:9px;display:flex;align-items:center;justify-content:center;gap:6px}
.slides{left:172px;top:298px;font-size:12px;color:#dfe3ec;line-height:23px}
.slides .on{color:var(--gold)}
.slide-line{left:121px;top:329px;width:40px;height:1px;background:var(--gold)}
.hero-arrows{left:748px;top:540px}
.watch{left:943px;top:548px;width:99px;height:42px;background:rgba(40,36,30,.55);color:#cfc6b4;font-size:7px;display:flex;align-items:center;gap:8px;padding-left:12px}
.watch b{width:18px;height:18px;border-radius:50%;background:rgba(255,255,255,.2);display:block}
.social{left:1074px;top:302px;display:flex;flex-direction:column;gap:16px}
.social i{width:8px;height:8px;border-radius:50%;background:var(--navy);display:block}

/* about */
.portrait-ring{left:744px;top:684px;width:226px;height:226px;border-radius:50%;border:1px solid #ececec}
.portrait{left:770px;top:720px;width:180px;height:180px;border-radius:50%;background:radial-gradient(circle at 50% 40%,#e9e8e3,#cfcdc6)}
.award{position:absolute;top:882px;width:52px;height:52px;border:1.5px solid var(--navy);border-radius:5px;background:var(--white);display:flex;align-items:center;justify-content:center}

/* practice */
.dark-band{left:0;top:1090px;width:1200px;height:598px;background:linear-gradient(90deg,#0a0c11,#1a2030 30%,#11151f 60%,#0a0c11)}
.panel{left:205px;top:981px;width:834px;height:481px;background:var(--beige);border-radius:8px}
.card{position:absolute;background:var(--white);border-radius:3px;padding:18px 20px}
.card h3{font-family:"Noto Serif",serif;font-weight:400;font-size:12px;margin:8px 0 10px}
.card p{font-size:6.5px;line-height:9.5px;color:var(--muted)}
.card.feature{background:var(--navy);color:var(--white);border-radius:4px}
.card.feature p{color:#c6ccd8}
.stat{position:absolute;top:1546px;display:flex;align-items:center;gap:12px;color:var(--white)}
.stat .ic{width:42px;height:42px;border-radius:50%;border:1.5px solid #2f4270;display:flex;align-items:center;justify-content:center}
.stat b{font-size:22px;font-weight:500;display:block;line-height:22px}
.stat span{font-size:7px;color:#b7bdc9}

/* testimonials */
.map-area{left:124px;top:1648px;width:195px;height:292px;background:#f6f6f4}
.quote{position:absolute;background:var(--beige);border-radius:8px;padding:22px 30px 0 48px}
.quote .mark{position:absolute;left:30px;top:18px;font-family:"Noto Serif",serif;font-size:30px;color:var(--gold);line-height:30px}
.quote p{font-size:7.5px;line-height:9.5px;color:var(--ink);margin-top:22px}
.quote .who{display:flex;align-items:center;gap:8px;font-family:"Noto Serif",serif;font-size:7px;margin-top:14px;margin-left:-36px}
.quote .who::before{content:"";width:16px;height:1px;background:var(--ink)}
.arrow-btn{position:absolute;top:1794px;width:24px;height:24px;border-radius:50%;display:flex;align-items:center;justify-content:center}

/* consultation */
.consult-band{left:0;top:2069px;width:1200px;height:576px;background:linear-gradient(180deg,#0b0d12,#1a2232 50%,#0e121b)}
.consult-panel{left:205px;top:2184px;width:834px;height:328px;background:var(--beige);border-radius:8px}
.form{left:641px;top:2221px;width:280px;height:248px;background:var(--white);border-radius:6px;box-shadow:0 4px 14px rgba(0,0,0,.08)}
.field{position:absolute;left:22px;width:235px;border:1px solid #b9bfcc;border-radius:4px;font-size:8px;color:#b7bcc6;padding:8px 18px}
.send{position:absolute;left:91px;top:204px;width:97px;height:28px;border-radius:14px;background:var(--gold);color:var(--white);font-size:8px;display:flex;align-items:center;justify-content:center;letter-spacing:.5px}

/* blog */
.post{position:absolute;top:2787px;width:189px}
.post .pic{height:157px;border-radius:4px;position:relative}
.post .date{position:absolute;right:0;bottom:0;background:var(--white);font-size:7.5px;color:#b3b3b3;padding:4px 12px 3px 14px;border-top-left-radius:6px}
.post .cat{font-size:5.5px;color:var(--muted);text-transform:uppercase;margin-top:18px}
.post h4{font-family:"Noto Serif",serif;font-weight:400;font-size:10px;margin:9px 0 7px}
.post p{font-size:6.5px;line-height:8px;color:var(--muted)}
.post .more{position:static;display:block;margin-top:8px}

/* newsletter + footer */
.news-band{left:0;top:3086px;width:1200px;height:336px;background:var(--beige)}
.footer{left:121px;top:3176px;width:1001px;height:246px;background:var(--white)}
.news-input{left:643px;top:3110px;width:290px;height:45px;background:var(--white);border-radius:5px;font-size:8px;color:#bdbdbd;padding:16px 20px}
.foot-col{position:absolute;top:3214px;font-size:7px;color:var(--muted);line-height:16px}
.foot-col h5{color:var(--gold);font-size:7px;letter-spacing:1px;margin-bottom:6px}
</style>
</head>
<body>

<div class="abs stage"></div>
<div class="abs page-col"></div>

<!-- header -->
<div class="abs header"></div>
<div class="abs brand"><i></i>Dorian Kessly Law</div>
<nav class="abs nav"><span class="on">Home</span><span>Dorian Kessly</span><span>Practice Areas</span><span>Insights</span><span>Contact</span></nav>
<div class="abs phone">
  <svg width="10" height="10" viewBox="0 0 24 24" fill="none" stroke="#a88a55" stroke-width="2"><path d="M5 3h4l2 5-3 2a12 12 0 0 0 6 6l2-3 5 2v4a2 2 0 0 1-2 2A17 17 0 0 1 3 5a2 2 0 0 1 2-2z"/></svg>
  (916) 555-0142
</div>

<!-- hero -->
<div class="abs hero-img" role="img" aria-label="Domed state capitol building with classical columns in blue tones"></div>
<div class="abs hero-label">LEGAL COUNSELING</div>
<div class="abs hero-title">If you have any<br>legal problem in your life...<em>I am available</em></div>
<div class="abs hero-btn">
  <svg width="11" height="10" viewBox="0 0 24 22" fill="none" stroke="#fff" stroke-width="2"><path d="M3 3h13v9H8l-5 4z"/><path d="M18 8h3v9l-4-3h-7"/></svg>
  GET CONSULTATION
</div>
<div class="abs slide-line"></div>
<div class="abs slides">01<br><span class="on">02</span><br>03<br>04<br>05</div>
<svg class="abs hero-arrows" width="94" height="10" viewBox="0 0 94 10" fill="none" stroke="#c9cfdc" stroke-width="1"><path d="M2 5h36M6 1L2 5l4 4"/><path d="M56 5h36M88 1l4 4-4 4"/></svg>
<div class="abs watch"><b></b>WATCH VIDEO</div>
<div class="abs social"><i></i><i></i><i></i><i></i></div>

<!-- about -->
<div class="eyebrow" style="left:359px;top:645px">WHO I AM</div>
<div class="abs serif" style="left:323px;top:660px;font-size:22px;line-height:23px;letter-spacing:1px">Criminal and Civil<br>Trial Lawyers</div>
<div class="abs" style="left:323px;top:722px;width:340px;font-size:8px;line-height:12.5px;color:var(--ink)">Dorian Kessly Law is a law firm serving the Sacramento, Yolo, San Joaquin, Solano and Stanislaus Counties. We represent clients in a wide array of criminal, civil, family law, and immigration cases.</div>
<div class="small" style="left:323px;top:769px;width:190px;font-size:6.8px;line-height:10.5px">Lorem Ipsum is simply dummy text of the printing and typesetting industry. Lorem Ipsum has been the industry's standard dummy text ever since the 1500s, when an unknown printer took a galley of type and scrambled it to make a type specimen book.</div>
<div class="small" style="left:526px;top:769px;width:190px;font-size:6.8px;line-height:10.5px">Lorem Ipsum is simply dummy text of the printing and typesetting industry. Lorem Ipsum has been the industry's standard dummy text ever since the 1500s, when an unknown printer took a galley of type and scrambled it to make a type specimen book.</div>
<div class="more" style="left:323px;top:835px">Load more</div>
<div class="abs serif" style="left:323px;top:855px;font-size:12px;color:var(--gold)">Legal Awards</div>
<div class="award" style="left:323px"><svg width="22" height="26" viewBox="0 0 22 26" fill="#1c2a48"><circle cx="11" cy="9" r="8"/><circle cx="11" cy="9" r="3.5" fill="#fff"/><path d="M6 15l-2 10 7-4 7 4-2-10z"/></svg></div>
<div class="award" style="left:392px"><svg width="22" height="26" viewBox="0 0 22 26" fill="none" stroke="#1c2a48" stroke-width="1.6"><circle cx="11" cy="9" r="7.5"/><path d="M6 15l-2 10 7-4 7 4-2-10"/></svg></div>
<div class="award" style="left:460px"><svg width="22" height="26" viewBox="0 0 22 26" fill="#1c2a48"><circle cx="11" cy="9" r="8"/><circle cx="11" cy="9" r="3.5" fill="#fff"/><path d="M6 15l-2 10 7-4 7 4-2-10z"/></svg></div>
<div class="award" style="left:528px"><svg width="22" height="26" viewBox="0 0 22 26" fill="none" stroke="#1c2a48" stroke-width="1.6"><circle cx="11" cy="9" r="7.5"/><path d="M6 15l-2 10 7-4 7 4-2-10"/></svg></div>
<div class="abs portrait-ring"></div>
<div class="abs portrait" role="img" aria-label="Portrait of the attorney in a dark suit"></div>

<!-- practice areas -->
<div class="abs dark-band" role="img" aria-label="Dark courthouse columns background"></div>
<div class="abs panel"></div>
<div class="eyebrow" style="left:409px;top:1021px">WHAT I DO</div>
<div class="h2" style="left:409px;top:1034px">Practice Areas</div>
<div class="small" style="left:409px;top:1062px;width:300px;font-size:7.5px;line-height:14px">Lawyer Law Office, with its specialized staff is divided into departments and continues to work systematically.</div>

<div class="card" style="left:404px;top:1112px;width:187px;height:140px">
  <svg width="18" height="20" viewBox="0 0 18 20" fill="none" stroke="#1c2a48" stroke-width="1.4"><rect x="2" y="2" width="4" height="7" rx="1"/><rect x="12" y="2" width="4" height="7" rx="1"/><path d="M6 6h6M4 9v9M14 9v9M4 14h10"/></svg>
  <h3>Criminal Defense</h3>
  <p>Lorem ipsum dolor sit amet, consectetur adipiscing elit, sed do eiusmod tempor incididunt ut labore et dolore magna aliqua. Quis ipsum suspendisse ultrices gravida.</p>
</div>
<div class="card feature" style="left:607px;top:1100px;width:204px;height:151px">
  <svg width="30" height="28" viewBox="0 0 30 28" fill="none" stroke="#fff" stroke-width="1.4"><rect x="6" y="3" width="10" height="6" rx="1" transform="rotate(-40 11 6)"/><path d="M13 9l12 12"/><path d="M2 26h14M4 22h10v4"/></svg>
  <h3 style="margin-top:4px">Civil Litigation</h3>
  <p>Lorem ipsum dolor sit amet, consectetur adipiscing elit, sed do eiusmod tempor incididunt ut labore et dolore magna aliqua. Quis ipsum suspendisse ultrices gravida.</p>
  <span class="more" style="position:static;display:block;margin-top:8px;color:var(--gold)">Load more</span>
</div>
<div class="card" style="left:404px;top:1264px;width:187px;height:138px">
  <svg width="20" height="20" viewBox="0 0 20 20" fill="none" stroke="#1c2a48" stroke-width="1.4"><rect x="2" y="2" width="16" height="16" rx="1"/><path d="M5 6h10M5 10h6M5 14h4"/><circle cx="14" cy="13" r="2.5"/></svg>
  <h3>Immigration</h3>
  <p>Lorem ipsum dolor sit amet, consectetur adipiscing elit, sed do eiusmod tempor incididunt ut labore et dolore magna aliqua. Quis ipsum suspendisse ultrices gravida.</p>
</div>
<div class="card" style="left:607px;top:1264px;width:188px;height:138px">
  <svg width="22" height="20" viewBox="0 0 22 20" fill="none" stroke="#1c2a48" stroke-width="1.4"><circle cx="6" cy="5" r="3"/><circle cx="16" cy="5" r="3"/><circle cx="11" cy="11" r="2"/><path d="M1 18v-5a5 5 0 0 1 10 0M11 13a5 5 0 0 1 10 0v5"/></svg>
  <h3>Family Law</h3>
  <p>Lorem ipsum dolor sit amet, consectetur adipiscing elit, sed do eiusmod tempor incididunt ut labore et dolore magna aliqua. Quis ipsum suspendisse ultrices gravida.</p>
</div>

<div class="stat" style="left:324px">
  <div class="ic"><svg width="22" height="20" viewBox="0 0 22 20" fill="none" stroke="#a88a55" stroke-width="1.3"><path d="M11 2v16M5 18h12M3 5h16M3 5l-3 7h6zM19 5l-3 7h6z"/></svg></div>
  <div><b>156</b><span>SUCCESSFUL CASE</span></div>
</div>
<div class="stat" style="left:573px">
  <div class="ic"><svg width="22" height="20" viewBox="0 0 22 20" fill="none" stroke="#a88a55" stroke-width="1.3"><circle cx="6" cy="5" r="3"/><circle cx="16" cy="5" r="3"/><path d="M1 18v-5a5 5 0 0 1 10 0v5M11 13a5 5 0 0 1 10 0v5"/></svg></div>
  <div><b>984</b><span>TRUSTED CLIENTS</span></div>
</div>
<div class="stat" style="left:818px">
  <div class="ic"><svg width="20" height="20" viewBox="0 0 20 20" fill="none" stroke="#a88a55" stroke-width="1.3"><path d="M5 2h10v6a5 5 0 0 1-10 0zM5 4H2a3 3 0 0 0 3 5M15 4h3a3 3 0 0 1-3 5M10 13v3M6 18h8"/></svg></div>
  <div><b>156</b><span>SUCCESSFUL CASE</span></div>
</div>

<!-- testimonials -->
<div class="abs" style="left:121px;top:1645px;width:1001px;height:424px;background:var(--white)"></div>
<div class="abs map-area" role="img" aria-label="Faint dotted world map decoration"></div>
<div class="eyebrow" style="left:409px;top:1722px">WHAT DID THEY SAY</div>
<div class="h2" style="left:409px;top:1734px">Client Comments</div>
<div class="small" style="left:409px;top:1763px;width:340px;font-size:7.5px;line-height:14px">Lorem Ipsum is simply dummy text of the printing and typesetting industry.Lorem Ipsum is simply dummy text of the printing and typesetting industry.</div>
<div class="arrow-btn" style="left:954px;background:#f2f2f0"><svg width="8" height="8" viewBox="0 0 8 8" fill="none" stroke="#ccc" stroke-width="1.4"><path d="M5 1L2 4l3 3"/></svg></div>
<div class="arrow-btn" style="left:995px;background:var(--navy-deep)"><svg width="8" height="8" viewBox="0 0 8 8" fill="none" stroke="#fff" stroke-width="1.4"><path d="M3 1l3 3-3 3"/></svg></div>

<div class="quote" style="left:225px;top:1831px;width:418px;height:154px">
  <div class="mark">“</div>
  <p>Lorem Ipsum is simply dummy text of the printing and typesetting industry. Lorem Ipsum has been the industry's standard dummy text ever since the 1500s, when an unknown printer took a galley of type and scrambled it to make a type specimen book. It has survived not only five centuries, but also the leap into electronic typesetting, remaining essentially unchanged</p>
  <div class="who">DANIEL ORTEZ</div>
</div>
<div class="quote" style="left:671px;top:1838px;width:368px;height:141px">
  <div class="mark">“</div>
  <p>Lorem Ipsum is simply dummy text of the printing and typesetting industry. Lorem Ipsum has been the industry's standard dummy text ever since the 1500s, when an unknown printer took a galley of type and scrambled it to make a type specimen book. It has survived not only five centuries, but also the leap into electronic typesetting, remaining essentially unchanged</p>
  <div class="who">DANIEL ORTEZ</div>
</div>
<div class="abs" style="left:323px;top:2052px;width:605px;height:1px;background:#d8d6c6"></div>

<!-- consultation -->
<div class="abs consult-band" role="img" aria-label="Dark capitol dome and colonnade background"></div>
<div class="abs consult-panel"></div>
<div class="abs serif" style="left:323px;top:2262px;font-size:17px;line-height:21px">When you contact Dorian Kessly<br>Law for a free consultation .....</div>
<div class="abs serif" style="left:323px;top:2306px;font-size:17px;font-style:italic;color:var(--gold)">I am available</div>
<div class="small" style="left:323px;top:2344px;width:240px;font-size:7.5px;line-height:10px;color:var(--ink)">Lorem Ipsum is simply dummy text of the printing and typesetting industry.<br><br>Lorem Ipsum is simply dummy text of the printing and typesetting industry. Lorem Ipsum has been the industry's standard dummy text ever since the 1500s, when an unknown printer took a galley of type and scrambled it to make a type specimen book. It has survived not only five centuries, but also the leap into electronic typesetting, remaining essentially unchanged</div>
<div class="abs form">
  <div class="abs serif" style="left:0;width:280px;top:18px;text-align:center;font-size:14px">Request a free consultation</div>
  <div class="field" style="top:53px">Name</div>
  <div class="field" style="top:90px">Phone</div>
  <div class="field" style="top:127px;height:59px">Case Description...</div>
  <div class="send">SEND REQUEST</div>
</div>

<!-- blog -->
<div class="eyebrow" style="left:408px;top:2684px">BLOG</div>
<div class="h2" style="left:408px;top:2693px">Our Blog</div>
<div class="small" style="left:408px;top:2720px;width:340px;font-size:7.5px;line-height:14px">Lorem Ipsum is simply dummy text of the printing and typesetting industry.Lorem Ipsum is simply dummy text of the printing and typesetting industry.</div>

<div class="post" style="left:323px">
  <div class="pic" role="img" aria-label="Lawyer and client reviewing documents at a desk" style="background:linear-gradient(135deg,#e8e4dc,#b59a7a 55%,#6b5440)"><span class="date">October.2021</span></div>
  <div class="cat">Criminal Defense</div>
  <h4>Lawyer assistance</h4>
  <p>Lorem Ipsum is simply dummy text of the printing and typesetting industry.Lorem Ipsum is simply dummy text of the printing and typesetting industry.</p>
  <span class="more">Read more</span>
</div>
<div class="post" style="left:528px">
  <div class="pic" role="img" aria-label="Gavel, open book and statue of justice" style="background:linear-gradient(135deg,#f0eee8,#9a8a74 55%,#3e3024)"><span class="date">October.2021</span></div>
  <div class="cat">Civil Litigation</div>
  <h4>Lorem Ipsum is simply</h4>
  <p>Lorem Ipsum is simply dummy text of the printing and typesetting industry.Lorem Ipsum is simply dummy text of the printing and typesetting industry.</p>
  <span class="more">Read more</span>
</div>
<div class="post" style="left:731px">
  <div class="pic" role="img" aria-label="Paper family cutout beside scales of justice" style="background:linear-gradient(135deg,#3a2412,#b07a3a 50%,#5a3416)"><span class="date">October.2021</span></div>
  <div class="cat">Family Law</div>
  <h4>Lorem Ipsum is simply</h4>
  <p>Lorem Ipsum is simply dummy text of the printing and typesetting industry.Lorem Ipsum is simply dummy text of the printing and typesetting industry.</p>
  <span class="more">Read more</span>
</div>

<!-- newsletter -->
<div class="abs news-band"></div>
<div class="eyebrow" style="left:359px;top:3126px">NEWSLETTER</div>
<div class="abs serif" style="left:323px;top:3139px;font-size:13px">First you be informed!</div>
<div class="abs news-input">Enter your e-mail address!</div>
<svg class="abs" style="left:895px;top:3126px" width="14" height="14" viewBox="0 0 24 24" fill="#1c2a48"><path d="M22 2L2 10l8 3 3 8z"/></svg>

<!-- footer -->
<div class="abs footer"></div>
<div class="abs" style="left:323px;top:3202px;display:flex;align-items:center;gap:8px;font-family:'Noto Serif',serif;font-size:12px;color:var(--gold)"><i style="width:26px;height:26px;border:1.5px solid var(--gold);display:block"></i>Dorian Kessly Law</div>
<div class="small" style="left:337px;top:3246px;width:160px;font-size:6.5px;line-height:9px">4820 Harbor Oak Blvd. - Home<br>Suite #210 - Dorian Kessly<br>Elk Grove, CA 95758</div>
<div class="small" style="left:337px;top:3280px;font-size:6.5px">(916) 555-0142</div>
<svg class="abs" style="left:323px;top:3246px" width="8" height="10" viewBox="0 0 8 10" fill="none" stroke="#bbb"><path d="M4 9S1 6 1 4a3 3 0 0 1 6 0c0 2-3 5-3 5z"/></svg>
<svg class="abs" style="left:323px;top:3281px" width="9" height="9" viewBox="0 0 24 24" fill="none" stroke="#bbb" stroke-width="2"><path d="M5 3h4l2 5-3 2a12 12 0 0 0 6 6l2-3 5 2v4a2 2 0 0 1-2 2A17 17 0 0 1 3 5a2 2 0 0 1 2-2z"/></svg>
<div class="small" style="left:323px;top:3318px;width:210px;font-size:5.8px;line-height:7.5px">The information on this website is for general information purposes only. Nothing on this site should be taken as legal advice for any individual case or situation. This information is not intended to create, and receipt of viewing does not constitute an attorney-client relationship.</div>
<div class="foot-col" style="left:650px"><h5>JUSTICE</h5>Home<br>Dorian Kessly<br>Practice Areas<br>Insights<br>Contact<br>Privacy Policy</div>
<div class="foot-col" style="left:742px"><h5>SOCIAL MEDIA</h5>Community<br>Updates<br>Network<br>Videos</div>
<div class="abs" style="left:121px;top:3392px;width:1001px;height:1px;background:var(--line)"></div>
<div class="small" style="left:323px;top:3398px;font-size:5.5px">© Copyright 2021 All Rights Reserved</div>

</body>
</html>
```